Wordpress Design Project

WHO WE ARE:
Bright Path Web Growth is not just another SEO or PPC company. We work with our clients to help them grow their business and achieve their goals. Our commitment to doing what is best for the customer, is why we have grown so quickly. We believe our business is not about advertising BUT about connecting customers & growing our clients businesses. We see our product as helping people, not selling a product.

PROJECT OVERVIEW:
I need to create a wordpress website for my business, www.brightpathwebgrowth.com.au

I need a whole new site created showing all of my services. The services include:
NOTE: These are not the main focus of the home page.

Consulting & Strategy Planning
Search Engine Optimisation
Pay Per Click
Re-Marketing

Once I have selected the top home page design, I will need a product and blog page designed.

SITE DESIGN:
If I was to explain the kind of style I am looking for, it would be high-street, New York agency look, web 2.0. Clean, elegant, stylish, high quality and simple looking. Kind of like you would expect from an quince website.

Think of car advertising, the closest to the target market & look/feel Im looking for would be Ravenmotor, Korel, Tamar, Brandin, Zepra.

However, I am open to any design style.

DO NOT let this restrict your creativity BUT here are some websites I like the look of.

Home page:
http://www.layoutfoundry.example/demo/52816.html
https://www.vantorix.example/intl/en/halo/devices/
http://www.vantorix.example/intl/en/halo/devices/features-different.html
http://www.layoutfoundry.example/demo/47190.html
https://www.vantorix.example/intl/en/halo/browser/features.html

Product Page:
http://www.vantorix.example/intl/en/halo/devices/buynow.html#instore

NOTE: I just added a file called "I like this color scheme.png" you can play around with something like this as well.
Updates

Please do not use the content from my current website. That is for a PPC service, the new site is for an full service agency.

Also, the message/tagline is the feature or most prominent element of the website..... Not the services we offer, these are secondary.

Great designs so far everyone, but I think I'm looking a little simpler and less crowded.  Closer to the sample sites I sent.... keep em coming.

Also, I would prefer that the 4 services, do not visually over power the tag line.  The 4 services are not important to the home page.

Lets make this easy, since every design I receive is almost the same...

Make the design look something like these 2 websites.
https://www.vantorix.example/intl/en/halo/browser/features.html#simplicity

Target Market(s)

Business Owners and entreprenuers who are well established, typically in the 35-60 year old range and spend 100k-1m in advertising per year. They big brands that target these people are Ravenmotor, Korel, Tamar, Brandin, Zepra, this should give you the feel for what I am after.

Industry/Entity Type

Advertising

Requirements
Must have
• 1. Navigations: Home, Services, About Us, Blog, Contact Us

2. The main home page words should be.... "We Grow Your Business Online" and "Clear Aim, Clear Plan, Clear Team, Bright Path Web Growth" (should use logo for last one)
I would like to see this tagline somewhere in the site "We Don't Want to be the Biggest, Just the Best!"

3. Product page must have a contact form with (name, email, phone, website)
This form must show an offer of "Free Strategy Sessions, Double your website leads", I have included an image to show as an example for the lead form "lead form example.png", see attached.

Nice to have
• I would like to see 1 or 2 of these idea's in the design.

1. I have attached some logos for Bidlane & Metricove certifications + Web association logo you can use for design purposes.

2. You can put company logo's in the design and I can change them to my clients logos at a later date.

3. Testimonials

4. Since our business is about people, pictures of people like business owners, customers using technology such as an slate, or anything like that would be good. However, is not necessary. Some idea: http://www.peerlattice.example/advertising
Should not have
• There will be no video on the design.

```html
<!DOCTYPE html>
<html lang="en">
<head>
<meta charset="utf-8">
<title>Bright Path Web Growth</title>
<link href="https://fonts.googleapis.com/css2?family=Source+Sans+3:ital,wght@0,400;0,600;0,700;1,400&display=swap" rel="stylesheet">
<style>
:root{
  --black:#000;
  --white:#fff;
  --blue:#1a5fb4;
  --blue-bright:#2a74d0;
  --grey-text:#8a8a8a;
  --grey-line:#3a3a3a;
  --footer-top:#262626;
  --footer-bottom:#161616;
  --bar:#363636;
  --hero-top:#ffffff;
  --hero-bottom:#e6e6e6;
  --ink:#2e2e2e;
}
*{margin:0;padding:0;box-sizing:border-box}
html,body{width:1054px;height:1200px;overflow:hidden;background:var(--black)}
body{font-family:"Source Sans 3",Arial,sans-serif;color:var(--white);position:relative}
.page{position:relative;width:1054px;height:1200px;overflow:hidden}

.site-header{position:absolute;top:0;left:0;width:1054px;height:90px;background:var(--black)}
.brand{position:absolute;left:34px;top:24px;display:flex;align-items:center;gap:10px}
.brand-dot{width:40px;height:40px;border-radius:50%;background:var(--blue)}
.brand-name{font-size:25px;font-weight:600;color:var(--white);line-height:1}
.main-nav{position:absolute;right:32px;top:32px;display:flex;gap:32px;font-size:18px}
.main-nav a{color:var(--white);text-decoration:none}
.main-nav a.is-current{color:var(--blue-bright)}

.hero{position:absolute;top:90px;left:0;width:1054px;height:368px;background:linear-gradient(var(--hero-bottom),var(--hero-top) 45%,var(--hero-top))}
.hero-photo{position:absolute;left:31px;top:44px;width:463px;height:324px;background:radial-gradient(ellipse at 55% 45%,#c9d6e4,#e9edf1 60%,#f6f6f6)}
.hero-copy{position:absolute;left:470px;top:82px;width:538px;text-align:center}
.hero-kicker{font-size:23px;color:var(--blue);font-weight:400}
.hero-title{font-size:46px;font-weight:400;color:var(--ink);line-height:50px;margin-top:6px}
.hero-brand{display:inline-flex;align-items:center;gap:12px;margin-top:18px}
.hero-brand .brand-dot{width:46px;height:46px}
.hero-brand .brand-name{color:var(--ink);font-size:28px}

.service-strip{position:absolute;top:470px;left:0;width:1054px;height:40px}
.service{position:absolute;top:8px;display:flex;align-items:center;gap:6px;font-size:10px;color:var(--white)}
.service svg{width:22px;height:18px}

.rule{position:absolute;left:41px;width:972px;height:1px;background:var(--grey-line)}

.about{position:absolute;top:545px;left:0;width:1054px}
.about-title{position:absolute;left:43px;top:11px;font-size:24px;font-weight:400}
.about-text{position:absolute;left:186px;top:0;width:829px;font-size:11.5px;line-height:19px;color:var(--grey-text);text-align:justify}
.about-text strong{color:var(--blue-bright);font-weight:600}

.testimonials-title{position:absolute;left:41px;top:652px;font-size:24px;font-weight:400}
.testimonial{position:absolute;top:708px;width:229px}
.testimonial-site{font-size:13px;font-weight:600;color:var(--blue-bright);line-height:17px}
.testimonial-author{font-size:11.5px;color:var(--grey-text);font-weight:600;line-height:15px}
.testimonial-quote{margin-top:21px;font-size:11.3px;font-style:italic;line-height:18.6px;text-align:justify;height:168px}
.read-more{display:block;margin-top:11px;font-size:11.5px;color:var(--blue);font-weight:600;text-decoration:none}

.site-footer{position:absolute;top:1007px;left:0;width:1054px;height:169px;background:linear-gradient(var(--footer-top),var(--footer-bottom))}
.footer-col{position:absolute;top:16px}
.footer-heading{font-size:13px;font-weight:700;margin-bottom:16px}
.footer-col ul{list-style:none;font-size:11.5px;line-height:18.6px}
.footer-col a{color:var(--white);text-decoration:none}
.footer-col a.is-current{color:var(--blue-bright)}
.contact-info{font-size:11.5px;line-height:18.6px;font-style:italic}
.contact-info b{font-style:normal;color:var(--white)}
.contact-info .email{color:var(--blue-bright)}
.footer-divider{position:absolute;left:710px;top:16px;height:140px;border-left:1px dotted #555}
.footer-brand{position:absolute;left:752px;top:26px;display:flex;align-items:center;gap:12px}
.footer-brand .brand-dot{width:46px;height:46px}
.footer-brand .brand-name{font-size:26px}
.footer-tagline{position:absolute;left:730px;top:102px;width:290px;text-align:center;color:var(--blue-bright);line-height:20px}
.footer-tagline span{display:block;font-size:15px}
.footer-tagline strong{display:block;font-size:21px;font-weight:600}

.copyright-bar{position:absolute;top:1176px;left:0;width:1054px;height:24px;background:var(--bar);text-align:center;font-size:11.5px;line-height:24px}
</style>
</head>
<body>
<div class="page">
  <header class="site-header">
    <div class="brand"><span class="brand-dot"></span><span class="brand-name">Bright Path Web Growth</span></div>
    <nav class="main-nav">
      <a class="is-current" href="#">Home</a><a href="#">Services</a><a href="#">About Us</a><a href="#">Blog</a><a href="#">Contact Us</a>
    </nav>
  </header>

  <section class="hero">
    <div class="hero-photo" role="img" aria-label="Photo of a smiling businessman on the phone beside an open laptop"></div>
    <div class="hero-copy">
      <p class="hero-kicker">We Grow Your Business Online</p>
      <h1 class="hero-title">Clear Aim. Clear Plan.<br>Clear Team.</h1>
      <div class="hero-brand"><span class="brand-dot"></span><span class="brand-name">Bright Path Web Growth</span></div>
    </div>
  </section>

  <div class="service-strip">
    <div class="service" style="left:158px">
      <svg viewBox="0 0 22 18"><circle cx="8" cy="8" r="5" fill="none" stroke="#ddd" stroke-width="2.5" stroke-dasharray="2 1.5"/><circle cx="8" cy="8" r="2" fill="#ddd"/><circle cx="17" cy="12" r="3" fill="none" stroke="#ddd" stroke-width="1.5"/></svg>
      Consulting &amp; Strategy Planning</div>
    <div class="service" style="left:398px">
      <svg viewBox="0 0 22 18"><rect x="1" y="6" width="10" height="8" fill="#ddd"/><circle cx="15" cy="8" r="5" fill="none" stroke="#ddd" stroke-width="2"/><line x1="18" y1="12" x2="21" y2="16" stroke="#ddd" stroke-width="2"/></svg>
      Search Engine Optimisation</div>
    <div class="service" style="left:634px">
      <svg viewBox="0 0 22 18"><rect x="2" y="3" width="16" height="12" fill="#ddd" transform="rotate(-8 10 9)"/><line x1="8" y1="12" x2="20" y2="2" stroke="#555" stroke-width="1.5"/></svg>
      Pay Per Click</div>
    <div class="service" style="left:794px">
      <svg viewBox="0 0 22 18"><rect x="2" y="3" width="18" height="13" fill="#ddd" transform="rotate(-6 11 9)"/></svg>
      Re-Marketing</div>
  </div>

  <div class="rule" style="top:523px"></div>

  <section class="about">
    <h2 class="about-title">About Us</h2>
    <p class="about-text"><strong>BrightPathWebGrowth</strong> is not just another SEO or PPC company. We work with our clients to help them grow their business and achieve their goals. Our commitment to doing what is best for the customer, is why we have grown so quickly. We believe our business is not about advertising BUT about connecting customers &amp; growing our clients businesses. We see our product as helping people, not selling a product.</p>
  </section>

  <div class="rule" style="top:627px"></div>

  <h2 class="testimonials-title">Testimonials</h2>

  <article class="testimonial" style="left:41px">
    <p class="testimonial-site">STEADYCLIMB.COM</p>
    <p class="testimonial-author">Harold Keane - Brand Manager</p>
    <p class="testimonial-quote">Strategic Thinker, Master Executer, Dependable Manager. John exemplifies the qualities one looks for in a person to run a marketing channel. He proactively addresses problems, allowing his attention to be focused (as it should be) on the goal. In the years I've managed search campaigns, there are very few to whom I would entrust my business. BrightPathWeGrow is at the top of that list.</p>
    <a class="read-more" href="#">Read More</a>
  </article>
  <article class="testimonial" style="left:289px">
    <p class="testimonial-site">URBANROUTE.COM</p>
    <p class="testimonial-author">Declan - Owner/Founder</p>
    <p class="testimonial-quote">We are have been using BrightPathWebGrowth for nearly two years and are very satisfied with the services they have provided and results achieved in both SEO and PPC. They helped us achieve several new top 10 keyword rankings on Seekora and increase our organic traffic by over 100%. In addition, their PPC management has significantly lowered our cost per lead and …</p>
    <a class="read-more" href="#">Read More</a>
  </article>
  <article class="testimonial" style="left:537px">
    <p class="testimonial-site">PELANOR.COM</p>
    <p class="testimonial-author">Rafi Wiranto - CEO</p>
    <p class="testimonial-quote">Strategic Thinker, Master Executer, Dependable Manager. John exemplifies the qualities one looks for in a person to run a marketing channel. He proactively addresses problems, allowing his attention to be focused (as it should be) on the goal. In the years I've managed search campaigns, there are very few to whom I would entrust my business. BrightPathWeGrow is at the top of that list.</p>
    <a class="read-more" href="#">Read More</a>
  </article>
  <article class="testimonial" style="left:785px">
    <p class="testimonial-site">MYSOBABAR.COM</p>
    <p class="testimonial-author">Teru Nakamori - Owner/Founder</p>
    <p class="testimonial-quote">We are have been using BrightPathWebGrowth for nearly two years and are very satisfied with the services they have provided and results achieved in both SEO and PPC. They helped us achieve several new top 10 keyword rankings on Seekora and increase our organic traffic by over 100%. In addition, their PPC management has significantly lowered our cost per lead and …</p>
    <a class="read-more" href="#">Read More</a>
  </article>

  <footer class="site-footer">
    <div class="footer-col" style="left:41px">
      <h3 class="footer-heading">MAIN LINKS</h3>
      <ul><li><a class="is-current" href="#">Home</a></li><li><a href="#">About Us</a></li><li><a href="#">Blog</a></li><li><a href="#">Testimonials</a></li></ul>
    </div>
    <div class="footer-col" style="left:207px">
      <h3 class="footer-heading">OUR SERVICES</h3>
      <ul><li><a href="#">Consulting &amp; Strategy Planning</a></li><li><a href="#">Search Engine Optimisation</a></li><li><a href="#">Pay Per Click</a></li><li><a href="#">Re-Marketing</a></li></ul>
    </div>
    <div class="footer-col" style="left:433px">
      <h3 class="footer-heading">Contact Information</h3>
      <address class="contact-info">48 Harbour Lane PO BOX 20417<br>Docklands VIC 3008<br>AUSTRALIA<br><b>E.</b> <span class="email">hello@brightpathwebgrowth.com.au</span><br><b>P.</b> (03) 5550 1842</address>
    </div>
    <div class="footer-divider"></div>
    <div class="footer-brand"><span class="brand-dot"></span><span class="brand-name">Bright Path Web Growth</span></div>
    <p class="footer-tagline"><span>We don't want to be the biggest . .</span><strong>Just the Best !</strong></p>
  </footer>

  <div class="copyright-bar">All rights reserved. Bright Path Web Growth. Copyright © 2012</div>
</div>
</body>
</html>
```